Seasons Inside a Restless Mind - Beyond the Storm, Toward Calm

I need a book cover, spine, and back cover. I need the book cover first for a book being written through pressloom.xyz. My sample shows a woman. I want a man in his 30s/40s. This is a book about me. I have suffered from bipolar disorder from adolescence to the present age of 75. I wasn't diagnosed until I was 50. Treatment has continued through the present. I'm not sure why I'm writing this, but I already have the title and subtitle for my book, but you know more than I do.
Target Market(s)
teens to 30's
Industry/Entity Type
none
Font styles to use
Serif
Requirements
Must have
- Man staring into oblivion or silhouette facing left and right Light and Dark
Nice to have
- See existing design- or man facing Left in the dark - facing right in the right
Should not have
- Woman

```html
<!DOCTYPE html>
<html lang="en">
<head>
<meta charset="utf-8">
<title>Seasons Inside a Restless Mind – Book Cover</title>
<link rel="stylesheet" href="https://fonts.googleapis.com/css2?family=Cinzel:wght@400;500&family=Open+Sans:wght@400&family=Barlow:wght@600&display=swap">
<style>
  :root {
    --ink: #000000;
    --white: #ffffff;
    --accent: #6aa6d6;
    --night: #0f1d2e;
    --night-deep: #050a12;
    --rule-grey: #9a9a9a;
    --placeholder: #b9b9b9;
  }
  * { margin: 0; padding: 0; box-sizing: border-box; }
  html, body { width: 1200px; height: 847px; overflow: hidden; background: var(--ink); }
  .cover {
    position: relative; width: 1200px; height: 847px; overflow: hidden;
    background: var(--ink);
    font-family: "Cinzel", "Times New Roman", serif;
    color: var(--white);
  }

  /* ---------- front ---------- */
  .front-bg {
    position: absolute; left: 632px; top: 0; width: 568px; height: 847px;
    background: radial-gradient(ellipse 70% 60% at 95% 15%, #1c3047 0%, var(--night) 35%, var(--night-deep) 70%, var(--ink) 100%);
  }
  .portrait {
    position: absolute; left: 784px; top: 0; width: 416px; height: 847px;
    background: radial-gradient(ellipse 55% 45% at 60% 30%, rgba(40,62,88,0.55) 0%, rgba(15,29,46,0.35) 50%, rgba(0,0,0,0) 100%);
  }
  .front-line { position: absolute; left: 671px; line-height: 1; white-space: nowrap; }
  .front-line.big { font-size: 84px; letter-spacing: 1px; }
  .front-line.small { font-size: 58px; color: var(--accent); letter-spacing: 2px; }
  .front-rule {
    position: absolute; left: 671px; top: 517px; width: 327px; height: 3px;
    background: linear-gradient(90deg, var(--white) 0%, var(--rule-grey) 70%, rgba(154,154,154,0) 100%);
  }
  .front-author {
    position: absolute; left: 1008px; top: 744px;
    font-family: "Barlow", "Arial", sans-serif; font-weight: 600;
    font-size: 25px; line-height: 32px; letter-spacing: 3px;
  }

  /* ---------- spine ---------- */
  .spine-title, .spine-author {
    position: absolute; transform: rotate(90deg); transform-origin: 0 0; white-space: nowrap;
  }
  .spine-title { left: 612px; top: 47px; font-size: 26px; line-height: 30px; }
  .spine-title .accent { color: var(--accent); font-size: 20px; }
  .spine-author {
    left: 632px; top: 664px;
    font-family: "Barlow", "Arial", sans-serif; font-weight: 600;
    font-size: 22px; line-height: 32px; letter-spacing: 3px;
  }

  /* ---------- back ---------- */
  .back-title { position: absolute; left: 37px; width: 491px; text-align: center; line-height: 1; white-space: nowrap; }
  .back-title .accent { color: var(--accent); font-size: 30px; }
  .back-title.row-a { top: 42px; font-size: 44px; }
  .back-title.row-b { top: 80px; font-size: 46px; }
  .back-title.row-c { top: 148px; font-size: 42px; }
  .back-title.row-d { top: 188px; font-size: 42px; }
  .back-rule {
    position: absolute; left: 125px; top: 135px; width: 320px; height: 2px;
    background: linear-gradient(90deg, rgba(154,154,154,0) 0%, var(--rule-grey) 40%, var(--rule-grey) 60%, rgba(154,154,154,0) 100%);
  }
  .blurb {
    position: absolute; left: 37px; top: 249px; width: 491px;
    font-family: "Open Sans", "Arial", sans-serif; font-size: 15px; line-height: 27px;
    letter-spacing: 1.4px; text-align: justify;
  }
  .blurb p { margin-bottom: 10px; }
  .blurb p.full { text-align-last: justify; }
  .author-photo { position: absolute; left: 36px; top: 646px; width: 148px; height: 113px; background: var(--placeholder); }
  .author-bio {
    position: absolute; left: 202px; top: 641px; width: 326px;
    font-family: "Open Sans", "Arial", sans-serif; font-size: 15px; line-height: 27px;
    letter-spacing: 1.4px; text-align: justify; text-align-last: justify;
  }
</style>
</head>
<body>
<main class="cover">

  <!-- back cover -->
  <h2 class="back-title row-a">Seasons <span class="accent">Inside a</span></h2>
  <h2 class="back-title row-b">Restless Mind</h2>
  <div class="back-rule"></div>
  <p class="back-title row-c"><span class="accent">Beyond the</span> Storm,</p>
  <p class="back-title row-d"><span class="accent">Toward</span> Calm</p>

  <div class="blurb">
    <p class="full">Lorem ipsum dolor sit amet, consectetur adipiscing elit, sed do eiusmod tempor incididunt ut labore et dolore magna aliqua. Quis ipsum suspendisse ultrices gravida. Risus commodo viverra maecenas accumsan lacus vel</p>
    <p class="full">Lorem ipsum dolor sit amet, consectetur adipiscing elit, sed do eiusmod tempor incididunt ut labore et dolore magna aliqua. Quis ipsum suspendisse ultrices gravida. Risus commodo viverra maecenas accumsan lacus vel</p>
    <p>Lorem ipsum dolor sit amet, consectetur adipiscing elit, sed do eiusmod tempor incididunt ut labore et dolore magna aliqua. Quis ipsum suspendisse ultrices gravida. Risus commodo viverra maecenas accumsan lacus vel facilisis.</p>
  </div>

  <div class="author-photo" role="img" aria-label="Author photo placeholder"></div>
  <p class="author-bio">Lorem ipsum dolor sit amet, consec&shy;tetur adipiscing elit, sed do eiusmod tempor incididunt ut labore et dolore magna aliqua. Quis ipsum sus&shy;pendisse ultrices gravida. Risus com-</p>

  <!-- spine -->
  <div class="spine-title">Seasons <span class="accent">Inside a</span> Restless Mind</div>
  <div class="spine-author">By Walter<br>Ashgrove</div>

  <!-- front cover -->
  <div class="front-bg"></div>
  <div class="portrait" role="img" aria-label="Silhouette of a man in his thirties or forties in profile, facing into darkness with soft light behind"></div>

  <h1>
    <span class="front-line big" style="top:202px">Seasons</span>
    <span class="front-line small" style="top:285px">Inside a</span>
    <span class="front-line big" style="top:342px">Restless</span>
    <span class="front-line big" style="top:421px">Mind</span>
  </h1>
  <div class="front-rule"></div>
  <p>
    <span class="front-line small" style="top:533px">Beyond the</span>
    <span class="front-line big" style="top:588px">Storm,</span>
    <span class="front-line small" style="top:670px">Toward</span>
    <span class="front-line big" style="top:727px">Calm</span>
  </p>
  <p class="front-author">BY WALTER<br>ASHGROVE</p>

</main>
</body>
</html>
```